Re-Design of Business Card for Marine Sales People

We are looking to Re-design our business cards to look like they are in the 21st century. We are a full service marina and sell a lot of new/used boats. May want a spot on the card for our 3 main brands we sell. A picture spot of the sales man would be nice, but not necessarily.

```html
<!DOCTYPE html>
<html lang="en">
<head>
<meta charset="utf-8">
<title>Harborline Marine – Business Card</title>
<link rel="stylesheet" href="https://fonts.googleapis.com/css2?family=Poppins:wght@500;600;700&family=Lato:wght@400&family=Lora:ital,wght@1,700&family=Mulish:ital,wght@1,600&display=swap">
<style>
  :root{
    --backdrop:#e4dbd2;
    --navy:#0f2d57;
    --navy-deep:#0b2246;
    --navy-light:#143a66;
    --sky:#2a8fc9;
    --ink:#222a33;
    --paper:#f6f6f6;
    --paper-shade:#ebebeb;
    --ghost:#e2e5ea;
  }
  *{margin:0;padding:0;box-sizing:border-box}
  html,body{width:1200px;height:1057px;overflow:hidden;background:var(--backdrop)}
  .canvas{position:relative;width:1200px;height:1057px}
  .card{position:absolute;left:258px;width:711px;height:406px;overflow:hidden;box-shadow:0 14px 28px rgba(60,45,30,.18)}
  .card--front{top:102px;background:linear-gradient(160deg,var(--paper) 30%,var(--paper-shade))}
  .card--back{top:549px;background:linear-gradient(135deg,var(--navy-deep),var(--navy-light))}

  .brand{position:absolute;display:flex;align-items:center;gap:10px;font-family:"Poppins",sans-serif;font-weight:600;letter-spacing:1px;white-space:nowrap}
  .brand__dot{width:14px;height:14px;border-radius:50%}
  .card--front .brand{left:46px;top:58px;font-size:31px;color:var(--navy)}
  .card--front .brand__dot{background:var(--navy)}
  .card--back .brand{left:90px;top:160px;font-size:30px;color:#fff}
  .card--back .brand__dot{background:#fff}

  .hull-watermark{position:absolute;left:190px;top:150px;width:490px;height:150px;border-radius:50%;background:radial-gradient(ellipse at center,var(--ghost) 0%,rgba(226,229,234,0) 70%)}

  .person{position:absolute;left:45px;top:178px}
  .person__name{font-family:"Poppins",sans-serif;font-weight:700;font-size:26px;color:var(--navy);letter-spacing:.3px;line-height:1.2}
  .person__tagline{font-family:"Poppins",sans-serif;font-weight:500;font-size:16px;color:var(--sky);line-height:1.1}

  .contact{position:absolute;left:45px;font-family:"Lato",sans-serif;font-size:16px;color:var(--ink);line-height:20.5px}
  .contact--address{top:241px;font-style:normal}
  .contact--lines{top:295px;list-style:none}
  .contact--lines li{display:flex;align-items:center;gap:6px;height:23.5px}
  .contact svg{width:13px;height:14px;fill:var(--sky)}

  .website{position:absolute;right:35px;top:342px;font-family:"Lato",sans-serif;font-size:16px;color:var(--navy)}
  .website__domain{color:var(--sky)}
  .accent-bar{position:absolute;left:453px;top:375px;width:223px;height:31px;background:var(--navy)}

  .motto{position:absolute;left:470px;top:153px;width:150px;text-align:center;font-family:"Lora",serif;font-style:italic;font-weight:700;color:#fff;font-size:17px;line-height:1}
  .motto__line{display:block}
  .motto__line + .motto__line{margin-top:18px}
  .locations{position:absolute;left:90px;top:249px;width:532px;height:29px;background:#fff;border-radius:0 0 14px 14px;display:flex;justify-content:space-between;align-items:center;padding:0 6px;font-family:"Mulish",sans-serif;font-style:italic;font-weight:600;font-size:15px;color:var(--navy)}
</style>
</head>
<body>
<main class="canvas">

  <section class="card card--front" aria-label="Business card front">
    <div class="brand"><span class="brand__dot"></span>HARBORLINE MARINE</div>
    <div class="hull-watermark" role="img" aria-label="Faint boat decoration"></div>

    <div class="person">
      <p class="person__name">DANIEL HART</p>
      <p class="person__tagline">Tagline Here</p>
    </div>

    <address class="contact contact--address">48 Cove Road<br>Lakeview, NH 03999</address>

    <ul class="contact contact--lines">
      <li><svg viewBox="0 0 14 14"><path d="M4 0h6a1.5 1.5 0 0 1 1.5 1.5v11A1.5 1.5 0 0 1 10 14H4a1.5 1.5 0 0 1-1.5-1.5v-11A1.5 1.5 0 0 1 4 0zm0 1.5v9.5h6V1.5zm3 10.3a.8.8 0 1 0 0 1.6.8.8 0 0 0 0-1.6z"/></svg>(555) 014-2270</li>
      <li><svg viewBox="0 0 14 14"><path d="M3 1l2 3-1.2 1.3a8 8 0 0 0 4.9 4.9L10 9l3 2-1 2.3C6 13.5.5 8 .7 2z"/></svg>(555) 014-2270</li>
      <li><svg viewBox="0 0 14 14"><path d="M0 3h14v8H0zm1.2 1.2L7 8l5.8-3.8V3.8H1.2z"/></svg>info@harborlinemarine.com</li>
    </ul>

    <p class="website">www.<span class="website__domain">harborlinemarine</span>.com</p>
    <div class="accent-bar"></div>
  </section>

  <section class="card card--back" aria-label="Business card back">
    <div class="brand"><span class="brand__dot"></span>HARBORLINE MARINE</div>
    <p class="motto"><span class="motto__line">“Riding Tides”</span><span class="motto__line">Since 1984</span></p>
    <div class="locations"><span>Lake Ashcombe, Lakeview, NH</span><span>Lake Merrow, Eastport, NH</span></div>
  </section>

</main>
</body>
</html>
```